Corvintal Real Estate Business Card

hello, we are a real estate company located in Los Angeles, california. we are a boutique, small company but we like a big corportate look. a simple, sleek, modern and progressive look. we would like the option of having a design that could include the real estate agents personal photo and also a design if the realtor desides not to have a photo. We also would like a hotizontal design.

Corvintal Properties
3817 N Halloway
West Hollywood, CA 90046
www.CorvintalRE.example

Glen Parrish
Broker
BRE # 04829175
(310) 555-0148
glen@corvintalre.example

Industry/Entity Type

Real Estate

```html
<!DOCTYPE html>
<html lang="en">
<head>
<meta charset="utf-8">
<title>Corvintal Real Estate Business Card</title>
<link rel="stylesheet" href="https://fonts.googleapis.com/css2?family=Open+Sans:wght@400;600&display=swap">
<style>
  :root {
    --page: #ece9e4;
    --card-white: #ffffff;
    --brand-blue: #1c63b4;
    --deep-blue: #0e4c98;
    --accent-cyan: #4fc3ec;
    --ink-blue: #1d5fae;
    --muted: #6b7480;
    --photo-top: #5b6a74;
    --photo-bottom: #2a2f33;
  }
  * { margin: 0; padding: 0; box-sizing: border-box; }
  html, body { width: 1200px; height: 1023px; overflow: hidden; }
  body {
    background: var(--page);
    font-family: "Open Sans", Arial, sans-serif;
    position: relative;
  }
  .card {
    position: absolute;
    left: 220px;
    width: 760px;
    height: 434px;
    overflow: hidden;
    box-shadow: 0 6px 18px rgba(0,0,0,0.18);
  }
  .card-front { top: 50px; background: var(--card-white); }
  .card-back {
    top: 540px;
    background: radial-gradient(ellipse at 35% 40%, #2f7fd0 0%, var(--brand-blue) 45%, var(--deep-blue) 100%);
  }

  /* Front */
  .front-band {
    position: absolute; left: 0; right: 0; bottom: 0; height: 150px;
    background: linear-gradient(180deg, #2170c2, var(--deep-blue));
    border-top: 10px solid var(--accent-cyan);
  }
  .front-column {
    position: absolute; top: 0; right: 0; width: 300px; bottom: 0;
    background: linear-gradient(180deg, #2170c2, var(--deep-blue));
    border-left: 10px solid var(--accent-cyan);
  }
  .agent-photo {
    position: absolute; top: 0; right: 22px; width: 258px; height: 168px;
    background: linear-gradient(180deg, var(--photo-top), var(--photo-bottom));
    border: 8px solid var(--accent-cyan);
    border-top: none;
  }
  .brand {
    position: absolute; left: 40px; top: 112px;
    display: flex; align-items: center; gap: 12px;
    color: var(--brand-blue);
    font-size: 34px; font-weight: 400; letter-spacing: -0.5px;
    white-space: nowrap;
  }
  .brand-dot {
    width: 26px; height: 26px; border-radius: 50%; background: var(--brand-blue);
  }
  .agent-name {
    position: absolute; left: 78px; top: 176px;
    color: var(--ink-blue); font-size: 22px; font-weight: 600; letter-spacing: 1.5px;
  }
  .agent-title {
    position: absolute; left: 78px; top: 208px;
    color: var(--muted); font-size: 13px; letter-spacing: 1.5px;
  }
  .agent-contact {
    position: absolute; left: 78px; bottom: 26px;
    color: #dce9f7; font-size: 14px; line-height: 1.55;
  }
  .office {
    position: absolute; right: 30px; top: 182px;
    text-align: right; color: #ffffff; font-size: 14px; line-height: 1.45;
    white-space: nowrap;
  }
  .office-name { color: var(--accent-cyan); font-weight: 600; }

  /* Back */
  .back-brand {
    position: absolute; right: 60px; bottom: 90px;
    display: flex; align-items: center; gap: 16px;
    color: #ffffff; font-size: 52px; font-weight: 400; letter-spacing: -0.5px;
    white-space: nowrap;
  }
  .back-brand .brand-dot { background: #ffffff; width: 36px; height: 36px; }
</style>
</head>
<body>
  <section class="card card-front">
    <div class="front-column"></div>
    <div class="front-band"></div>
    <div class="agent-photo" role="img" aria-label="Portrait photo of the agent"></div>

    <div class="brand"><span class="brand-dot"></span>Corvintal Properties</div>
    <div class="agent-name">GLEN PARRISH</div>
    <div class="agent-title">BROKER</div>

    <div class="agent-contact">
      BRE # 04829175<br>
      (310) 555-0148<br>
      glen@corvintalre.example
    </div>

    <div class="office">
      <div class="office-name">Corvintal Properties</div>
      3817 N Halloway<br>
      West Hollywood, CA 90046<br>
      www.CorvintalRE.example
    </div>
  </section>

  <section class="card card-back">
    <div class="back-brand"><span class="brand-dot"></span>Corvintal Properties</div>
  </section>
</body>
</html>
```